Lumora business card for a plastic surgeon

we need a business card for plastic surgeons that work on a clinic called LUMORA.
we want a clean design and the following informations: name of the doctor, doctor's registration number (called CRM), telephone, address, facebook, instagram.
Colors: white, blue tones, light brown/ coffee

facebook and instagram: lumoracirurgiaestetica

Industry/Entity Type

Business

Contact Information for Business Card

clean design

Font styles to use
Serif
Sans Serif
Other font styles liked:
• helvetica light

Colors
cee9f5
85cae6
85abd2
3276b5
cfeae6
cedeed
eaf1f7

Requirements
Must have
• doctor's name
• identification number (called CRM)
• contact (phone, facebook, instagram, address)

```html
<!DOCTYPE html>
<html lang="pt">
<head>
<meta charset="utf-8">
<title>Lumora – Cartão de Visita</title>
<link rel="stylesheet" href="https://fonts.googleapis.com/css2?family=Cinzel:wght@400;500&family=Open+Sans:wght@400;600;700&display=swap">
<style>
  :root {
    --bg: #e4e4e4;
    --card: #ffffff;
    --cyan: #22b8d8;
    --cyan-light: #2cc0de;
    --blue-deep: #1a6a94;
    --blue-mid: #1e93b8;
    --navy: #1d2f57;
    --grey-text: #4a4a4a;
  }
  * { margin: 0; padding: 0; box-sizing: border-box; }
  html, body {
    width: 1200px; height: 1200px; overflow: hidden;
    background: radial-gradient(circle at 50% 35%, #f2f2f2 0%, var(--bg) 75%);
    font-family: "Open Sans", Helvetica, Arial, sans-serif;
  }
  .canvas { position: relative; width: 1200px; height: 1200px; }

  .card {
    position: absolute; width: 540px; height: 320px;
    background: var(--card);
    box-shadow: 0 10px 28px rgba(0,0,0,0.16);
    overflow: hidden;
  }

  /* Back: brand side */
  .card--back { left: 600px; top: 110px; }
  .back-wordmark {
    position: absolute; left: 0; right: 0; top: 70px; text-align: center;
  }
  .back-wordmark .brand-name {
    font-family: "Cinzel", serif; font-weight: 400;
    font-size: 78px; letter-spacing: 4px; color: var(--cyan); line-height: 1;
  }
  .back-wordmark .brand-tagline {
    font-family: "Cinzel", serif; font-weight: 500;
    font-size: 25px; letter-spacing: 2px; color: var(--navy); margin-top: 10px;
  }
  .back-social {
    position: absolute; left: 0; right: 0; top: 232px;
    display: flex; align-items: center; justify-content: center; gap: 10px;
    font-size: 15px; color: var(--grey-text);
  }
  .back-social .dot {
    width: 14px; height: 14px; border-radius: 50%; background: var(--blue-mid);
  }

  /* Front: doctor side */
  .card--front { left: 60px; top: 500px; }
  .front-name {
    position: absolute; left: 250px; top: 38px;
    display: flex; align-items: baseline; gap: 10px;
  }
  .front-name .doctor {
    font-weight: 700; font-size: 30px; color: var(--cyan); letter-spacing: -0.5px;
  }
  .front-name .sep { font-size: 20px; color: #333; }
  .front-name .crm { font-weight: 700; font-size: 18px; color: #333; }
  .front-band {
    position: absolute; left: 0; right: 0; top: 125px; bottom: 0;
    background: linear-gradient(90deg, var(--blue-deep) 0%, var(--blue-mid) 100%);
  }
  .front-emblem {
    position: absolute; left: 90px; top: 70px; width: 150px; height: 150px;
    border-radius: 50%; background: var(--cyan-light);
  }
  .front-contact {
    position: absolute; left: 40px; bottom: 38px; color: #fff;
    font-size: 16px; line-height: 1.6;
  }
  .front-contact .address {
    border-bottom: 1px solid rgba(255,255,255,0.35); padding-bottom: 2px;
  }

  /* Standalone lockup */
  .lockup {
    position: absolute; left: 690px; top: 930px; width: 470px; text-align: center;
  }
  .lockup .brand-name {
    font-family: "Cinzel", serif; font-weight: 400;
    font-size: 96px; letter-spacing: 5px; color: var(--cyan); line-height: 1;
  }
  .lockup .rule {
    display: block; margin: 4px auto 0; width: 460px; height: 20px;
  }
  .lockup .brand-tagline {
    font-family: "Cinzel", serif; font-weight: 500;
    font-size: 34px; letter-spacing: 2px; color: var(--navy); margin-top: 2px;
  }
</style>
</head>
<body>
<main class="canvas">

  <section class="card card--back" aria-label="Verso do cartão">
    <div class="back-wordmark">
      <div class="brand-name">LUMORA</div>
      <div class="brand-tagline">CIRURGIA PLÁSTICA</div>
    </div>
    <div class="back-social">
      <span class="dot"></span>
      <span class="handle">lumoracirurgiaestetica</span>
    </div>
  </section>

  <section class="card card--front" aria-label="Frente do cartão">
    <div class="front-band"></div>
    <div class="front-emblem" role="img" aria-label="Emblema da clínica"></div>
    <div class="front-name">
      <span class="doctor">JOHN DOE</span>
      <span class="sep">|</span>
      <span class="crm">CRM</span>
    </div>
    <div class="front-contact">
      <div class="phone">1-234-567890</div>
      <div class="address">Dummy city, Dummy Country Land Dummy</div>
    </div>
  </section>

  <section class="lockup" aria-label="Assinatura da marca">
    <div class="brand-name">LUMORA</div>
    <svg class="rule" viewBox="0 0 460 20" aria-hidden="true">
      <path d="M0 12 Q230 2 460 12" fill="none" stroke="var(--cyan)" stroke-width="3"/>
    </svg>
    <div class="brand-tagline">CIRURGIA PLÁSTICA</div>
  </section>

</main>
</body>
</html>
```